Webdesign for an Health & Beauty Center

We need a new modern and elegant web design for the relaunch of the http://veskarin.at/ website.
The website is for a company which offer all services for a beuty center like epilation, cosmetics and more.
The new website should use big emotional background images and a modern menu.
All in all the website should give a female expression and the design should be clear and not playful.
The existing logo used be used for the new design, the base colours of the existing website could be used optionally.

Reason: Review of the designs together with the customer needs a little more time.

Industry/Entity Type
It Company
Look and feel
Each slider illustrates characteristics of the customer's brand and the style your logo design should communicate.

```html
<!DOCTYPE html>
<html lang="en">
<head>
<meta charset="utf-8">
<title>Veskarin – Health &amp; Beauty Center</title>
<link href="https://fonts.googleapis.com/css2?family=Lato:wght@300;400;700&display=swap" rel="stylesheet">
<style>
:root{
  --gold:#c8b07a;
  --gold-band:#d8c18f;
  --gold-title:#cdb98d;
  --sunday:#a9afbd;
  --ink-soft:#b9bec8;
  --nav:#b0b0b0;
  --accent:#e0a45a;
  --footer:#3b404e;
  --footer-line:#4c5262;
  --footer-text:#6b7182;
  --white:#ffffff;
}
*{margin:0;padding:0;box-sizing:border-box}
html,body{width:749px;height:1200px;overflow:hidden;background:var(--white)}
body{position:relative;font-family:'Lato',sans-serif;color:var(--ink-soft)}
.abs{position:absolute}

/* header */
.brand{left:115px;top:14px}
.brand-name{font-weight:300;font-size:27px;letter-spacing:3px;color:var(--gold);display:flex;align-items:center;gap:6px}
.brand-name i{display:inline-block;width:12px;height:12px;border-radius:50%;background:var(--gold)}
.brand-tag{font-size:7px;letter-spacing:1.5px;color:var(--gold);margin:6px 0 0 26px}
.social{right:115px;top:6px;display:flex;gap:6px}
.social span{width:14px;height:14px;background:var(--gold)}
.nav{right:115px;top:37px;display:flex;gap:11px;font-size:7.5px;color:var(--nav)}
.nav .active{color:var(--accent)}

/* hero */
.hero{left:0;top:81px;width:749px;height:253px;background:linear-gradient(110deg,#b88c74 0%,#d9b9a6 35%,#6b4a3e 60%,#8c4a8c 85%,#3a2a2e 100%)}
.cap-title{left:115px;top:172px;background:rgba(200,176,122,.85);color:var(--white);font-weight:700;font-size:8px;padding:6px 10px}
.cap-text{left:115px;top:203px;width:252px;background:rgba(200,176,122,.85);color:var(--white);font-size:6.8px;line-height:9.6px;padding:4px 10px}
.hero-arrow{top:199px;width:16px;height:16px;border-radius:50%;background:var(--white)}
.dots{left:357px;top:321px;display:flex;gap:4px}
.dots span{width:9px;height:9px;border-radius:50%;border:1px solid var(--white)}
.dots .on{background:var(--white)}

/* section titles */
.sec-title{left:0;width:749px;text-align:center;font-weight:300;font-size:15px;color:var(--gold-title)}
.sec-rule{left:358px;width:33px;height:1px;background:var(--gold)}

/* opening */
.days{left:115px;top:428px;display:flex;gap:7.5px}
.day{width:68px;text-align:center}
.day b{display:block;height:46px;line-height:46px;background:var(--gold);color:var(--white);font-weight:400;font-size:13px}
.day.closed b{background:var(--sunday)}
.day small{display:block;margin-top:9px;font-size:8px;color:#c6c6c6}

/* services */
.band{left:0;top:548px;width:749px;height:248px;background:linear-gradient(100deg,#d1b886,#dcc698 50%,#d4bc8a)}
.service{top:609px;width:164px;text-align:center;color:var(--white)}
.service .photo{height:94px}
.service h3{font-weight:300;font-size:10px;margin:13px 0 7px}
.service p{font-size:6.5px;line-height:11.2px}

/* testimonials */
.avatar{left:116px;top:905px;width:22px;height:22px;border-radius:50%;background:#8a6a52}
.who{left:148px;top:905px;font-size:7.5px;line-height:12px;color:var(--ink-soft)}
.quote{left:205px;top:895px;width:428px;text-align:center;font-size:8px;line-height:14px;color:var(--ink-soft)}
.qmark{font-size:18px;font-weight:700;color:#c7cbd3;line-height:0;vertical-align:-6px}
.t-nav{top:956px;width:14px;height:14px;background:var(--sunday)}

/* footer */
.footer{left:0;top:1017px;width:749px;height:183px;background:var(--footer)}
.f-head{top:1035px;font-weight:300;font-size:10px;color:#8e94a3}
.f-text{font-size:6px;line-height:9.6px;color:var(--footer-text)}
.f-icons{display:flex;gap:8px}
.f-icons span{width:14px;height:14px;background:#4e5465}
.thumb{width:36px;height:36px}
.field{background:#454a59;font-size:6px;color:var(--footer-text);padding:5px 6px}
.send{background:#454a59;font-size:6.5px;color:var(--footer-text);text-align:center;line-height:16px}
.f-rule{left:115px;top:1185px;width:519px;height:1px;background:var(--footer-line)}
.copy{left:115px;top:1189px;font-size:6px;color:var(--footer-text)}
</style>
</head>
<body>

<header>
  <div class="abs brand">
    <div class="brand-name"><i></i>veskarin</div>
    <div class="brand-tag">HEALTH &amp; BEAUTY CENTER</div>
  </div>
  <div class="abs social"><span></span><span></span><span></span><span></span></div>
  <nav class="abs nav">
    <span class="active">Home</span><span>About us</span><span>Services</span><span>Gallery</span><span>Care line</span><span>Offers</span><span>Price lists</span><span>Contact</span>
  </nav>
</header>

<section>
  <div class="abs hero" role="img" aria-label="Close-up of a woman having eyeshadow applied with a brush, surrounded by makeup palettes and purple carnations"></div>
  <div class="abs cap-title">Praesent pellentesque blandit turpis</div>
  <div class="abs cap-text">Integer mi quam, pellentesque quis velit id, tincidunt molestie felis. Quisque a erat nec ipsum dictum lobortis sed id massa. Integer dictum lobortis libero, in pellentesque erat congue at.</div>
  <svg class="abs hero-arrow" style="left:51px" viewBox="0 0 16 16"><circle cx="8" cy="8" r="8" fill="#fff"/><path d="M9 5 6 8l3 3" stroke="#999" fill="none"/></svg>
  <svg class="abs hero-arrow" style="left:681px" viewBox="0 0 16 16"><circle cx="8" cy="8" r="8" fill="#fff"/><path d="M7 5l3 3-3 3" stroke="#999" fill="none"/></svg>
  <div class="abs dots"><span class="on"></span><span></span><span></span></div>
</section>

<section>
  <h2 class="abs sec-title" style="top:377px">Opening Time</h2>
  <div class="abs sec-rule" style="top:403px"></div>
  <div class="abs days">
    <div class="day"><b>MON.</b><small>9:00 - 19:00</small></div>
    <div class="day"><b>TUE.</b><small>9:00 - 19:00</small></div>
    <div class="day"><b>WED.</b><small>9:00 - 19:00</small></div>
    <div class="day"><b>THU.</b><small>9:00 - 19:00</small></div>
    <div class="day"><b>FRI.</b><small>9:00 - 19:00</small></div>
    <div class="day"><b>SAT.</b><small>9:00 - 01:00</small></div>
    <div class="day closed"><b>SUN.</b><small>Closed</small></div>
  </div>
</section>

<section>
  <div class="abs band" role="img" aria-label="Faint gold-toned background photo of a woman"></div>
  <h2 class="abs sec-title" style="top:558px;color:var(--white)">Our Services</h2>
  <div class="abs sec-rule" style="top:585px;background:var(--white)"></div>
  <div class="abs service" style="left:115px">
    <div class="photo" role="img" aria-label="Make-up being applied to a woman's eye" style="background:linear-gradient(120deg,#5a3a34,#c49a88 45%,#8a3a8a)"></div>
    <h3>Make-up</h3>
    <p>Donec dictum sollicitudin ligula id molestie. Etiam ultricies nisl a lobortis varius. Etiam ullam-corper, turpis eu tincidunt laoreet, tellus nulla elementum arcu, quis tincidunt.</p>
  </div>
  <div class="abs service" style="left:292px">
    <div class="photo" role="img" aria-label="Wax strip epilation on a leg" style="background:linear-gradient(120deg,#e8b89a,#f3ddd0 55%,#f8efe8)"></div>
    <h3>Epilation</h3>
    <p>Nam bibendum rutrum nisl. Proin sit amet lorem ac tortor ornare vulputate. Nullam molestie ipsum ut mauris suscipit, in dapibus nisl luctus. Nam commodo semper pretium.</p>
  </div>
  <div class="abs service" style="left:470px">
    <div class="photo" role="img" aria-label="Woman relaxing during a back massage with candles" style="background:linear-gradient(120deg,#6a4428,#b8804e 50%,#e8cdb0)"></div>
    <h3>Massage</h3>
    <p>Duis dapibus iaculis facilisis. Curabitur facilisis ligula vitae iaculis volutpat. Integer rhoncus enim non dui dictum pretium. Duis fringilla, massa vul-putate feugiat tincidunt.</p>
  </div>
</section>

<section>
  <h2 class="abs sec-title" style="top:849px">Testimonials</h2>
  <div class="abs sec-rule" style="top:875px"></div>
  <div class="abs avatar" role="img" aria-label="Client portrait"></div>
  <div class="abs who">Mirela<br>Client</div>
  <p class="abs quote"><span class="qmark">&ldquo;</span> Duis dapibus iaculis facilisis curabitur facilisis ligula vitae iaculis volutpat. Integer rhoncus enim non dui dictum pretium, duis fringilla, massa vulputate feugiat tincidunt, turpis neque venenatis nulla, molestie tincidunt elit enim faucibus lacus. Nunc augue enim, convallis vitae auctor ut, ullamcorper posuere felis. <span class="qmark">&rdquo;</span></p>
  <svg class="abs t-nav" style="left:603px" viewBox="0 0 14 14"><rect width="14" height="14" fill="#a9afbd"/><path d="M8 4 5 7l3 3" stroke="#fff" fill="none"/></svg>
  <svg class="abs t-nav" style="left:620px" viewBox="0 0 14 14"><rect width="14" height="14" fill="#a9afbd"/><path d="M6 4l3 3-3 3" stroke="#fff" fill="none"/></svg>
</section>

<footer>
  <div class="abs footer"></div>
  <h4 class="abs f-head" style="left:115px">About Us</h4>
  <p class="abs f-text" style="left:115px;top:1061px;width:118px">Duis dapibus iaculis facilisis curabitur facilisis ligula vitae iaculis volutpat. Integer rhoncus enim non dui dictum pretium, duis fringilla, massa vulputate feugiat tincidunt, turpis neque venenatis nulla, molestie tincidunt elit enim faucibus lacus.<br><br>Nunc augue enim, convallis vitae auctor ut, ullamcorper posuere felis.</p>

  <h4 class="abs f-head" style="left:247px">Get in touch</h4>
  <p class="abs f-text" style="left:247px;top:1061px;width:120px">Veskarin - Health &amp; Beauty Center<br>218 Lindenhall Road, Suite 4<br>Graz 8010<br><br>&#9742;&nbsp; +43 316 555 0182<br>&#9993;&nbsp; contact@veskarin.com</p>
  <div class="abs f-icons" style="left:247px;top:1123px"><span></span><span></span><span></span><span></span></div>

  <h4 class="abs f-head" style="left:381px">Gallery</h4>
  <div class="abs thumb" style="left:381px;top:1062px;background:#c9a0a8" role="img" aria-label="Manicured nails"></div>
  <div class="abs thumb" style="left:421px;top:1062px;background:#e6c4a8" role="img" aria-label="Skin care treatment"></div>
  <div class="abs thumb" style="left:381px;top:1101px;background:#4a3034" role="img" aria-label="Make-up portrait"></div>
  <div class="abs thumb" style="left:421px;top:1101px;background:#c07aa0" role="img" aria-label="Beauty portrait"></div>

  <h4 class="abs f-head" style="left:470px">Contact us</h4>
  <div class="abs field" style="left:470px;top:1062px;width:79px;height:16px">Name</div>
  <div class="abs field" style="left:555px;top:1062px;width:79px;height:16px">Email</div>
  <div class="abs field" style="left:470px;top:1085px;width:164px;height:45px">Message</div>
  <div class="abs send" style="left:470px;top:1142px;width:56px;height:16px">Send</div>

  <div class="abs f-rule"></div>
  <p class="abs copy">©2014 Veskarin - Health &amp; Beauty Center. All Rights Reserved.</p>
</footer>

</body>
</html>
```